Business Card & Email Signature Design || Upmarket + Luxury

Riverlume Honey, a New Zealand Manuka Honey company needs a Business Card & Email Signature design.

Our logo's are attached in Gold & Black versions, feel free to be creative with how you use the logo and it's patterns in your design.

Style:
- Looking for an Elegant, Luxurious, Upmarket feel.
- Black/Matte Black Card, Gold Foil, UV Embossing

Information to Add:

- Logo
- Company Name: Riverlume Honey
- Name: Mattias Brovell
- Title: Creative Director
- Phone: +64 2919 58 617
- Email: mattias@riverlumehoney.example
- Website: www.riverlumehoney.example

- Socials: ***For email Signature Only***
- Facebook: https://www.facebook.com/riverlumehoney/
- Instagram: https://www.instagram.com/riverlumehoney/

Target Market(s)

Asia/Europe Luxury, Upmarket

Contact Information for Business Card

- Logo
- Name: Mattias Brovell
- Phone: +64 2919 58 617

Font styles to use
Other font styles liked:
• Champagne & Limousines (Attached)

Requirements
Must have
• Business Card & Email Signature Design.

Looking for a Sleek, Luxury, Upmarket Design.

```html
<!DOCTYPE html>
<html lang="en">
<head>
<meta charset="utf-8">
<title>Riverlume Honey – Business Card</title>
<link rel="stylesheet" href="https://fonts.googleapis.com/css2?family=Josefin+Sans:wght@300;400&display=swap">
<style>
  :root {
    --backdrop: #111112;
    --card: #1d1d1e;
    --card-edge: #2a2a2b;
    --gold: #c9a458;
    --font-main: "Josefin Sans", sans-serif;
  }
  * { margin: 0; padding: 0; box-sizing: border-box; }
  html, body { width: 1200px; height: 865px; overflow: hidden; background: var(--backdrop); }
  .canvas { position: relative; width: 1200px; height: 865px; font-family: var(--font-main); color: var(--gold); }

  .card {
    position: absolute; width: 600px; height: 343px;
    background: var(--card);
    border: 1px solid var(--card-edge);
    box-shadow: 0 18px 40px rgba(0,0,0,0.55);
  }
  .card--front { left: 70px; top: 100px; }
  .card--back { left: 530px; top: 470px; }

  /* Front */
  .brand {
    position: absolute; left: 40px; top: 110px; width: 290px;
    display: flex; flex-direction: column; align-items: center; gap: 18px;
  }
  .brand__dot { width: 58px; height: 58px; border: 1.5px solid var(--gold); border-radius: 50%; }
  .brand__name { font-weight: 300; font-size: 27px; letter-spacing: 3px; text-transform: uppercase; white-space: nowrap; }

  .divider { position: absolute; left: 345px; top: 92px; width: 1px; height: 120px; background: var(--gold); }

  .contact { position: absolute; left: 368px; top: 86px; width: 220px; }
  .contact__name { font-weight: 400; font-size: 21px; letter-spacing: 0.5px; text-transform: uppercase; }
  .contact__title { font-weight: 300; font-size: 11px; letter-spacing: 0.5px; text-transform: uppercase; margin-top: 3px; }
  .contact__rule { width: 8px; height: 1px; background: var(--gold); margin: 12px 0 8px; }
  .contact__list { list-style: none; }
  .contact__item { display: flex; align-items: center; gap: 8px; font-weight: 300; font-size: 11.5px; line-height: 19px; white-space: nowrap; }
  .contact__item svg { width: 10px; height: 10px; flex: none; }

  /* Back */
  .seal {
    position: absolute; left: 330px; top: 52px; width: 238px; height: 238px;
    border: 2px solid var(--gold); border-radius: 50%;
    display: flex; align-items: center; justify-content: center;
  }
  .seal__name { font-weight: 300; font-size: 17px; letter-spacing: 3px; text-transform: uppercase; text-align: center; line-height: 1.5; }
</style>
</head>
<body>
<main class="canvas">
  <section class="card card--front" aria-label="Business card front">
    <div class="brand">
      <span class="brand__dot"></span>
      <span class="brand__name">Riverlume Honey</span>
    </div>
    <span class="divider"></span>
    <div class="contact">
      <p class="contact__name">Mattias Brovell</p>
      <p class="contact__title">Creative Director</p>
      <div class="contact__rule"></div>
      <ul class="contact__list">
        <li class="contact__item">
          <svg viewBox="0 0 10 10" aria-hidden="true"><path d="M2 0.8 L3.6 2.8 L2.8 3.8 Q4 6.2 6.2 7.2 L7.2 6.4 L9.2 8 L8 9.4 Q2 8.6 0.6 2 Z" fill="var(--gold)"/></svg>
          +64 2919 58 617
        </li>
        <li class="contact__item">
          <svg viewBox="0 0 10 10" aria-hidden="true"><rect x="0.5" y="2" width="9" height="6.4" fill="none" stroke="var(--gold)"/><path d="M0.5 2 L5 5.6 L9.5 2" fill="none" stroke="var(--gold)"/></svg>
          mattias@riverlumehoney.example
        </li>
        <li class="contact__item">
          <svg viewBox="0 0 10 10" aria-hidden="true"><circle cx="5" cy="5" r="4.4" fill="none" stroke="var(--gold)"/><ellipse cx="5" cy="5" rx="1.9" ry="4.4" fill="none" stroke="var(--gold)"/><path d="M0.6 5 H9.4" stroke="var(--gold)"/></svg>
          www.riverlumehoney.example
        </li>
      </ul>
    </div>
  </section>

  <section class="card card--back" aria-label="Business card back">
    <div class="seal">
      <span class="seal__name">Riverlume<br>Honey</span>
    </div>
  </section>
</main>
</body>
</html>
```